Video Performance Case study

We need to design a double sided stats sheet for the presentation of data relating to the performance of videos that we have marketed. Front page can be very image based and the back page should be info graphics based. A3 would probably work best but open to larger sizes if necessary. The data that we need to present is Geographical, number of views, completion rate (%), short overview of what we did, sample URL's.
This flyer will be used as a sales tool to highlight the work that we have done so needs to look very cool and modern.
Will be printed as a two sider and distributed online via PDF
Ideally will be produced in InDesign but Photoshop is OK.

```html
<!DOCTYPE html>
<html lang="en">
<head>
<meta charset="utf-8">
<title>Video Performance Case Study</title>
<link rel="stylesheet" href="https://fonts.googleapis.com/css2?family=Roboto+Slab:wght@400;700;900&family=Roboto:wght@500&display=swap">
<style>
  :root {
    --paper: #fdfde6;
    --ink-deep: #0e5a82;
    --ink: #1d6a93;
    --ink-mid: #2f7ba3;
    --ink-soft: #5c9cbd;
    --ink-pale: #86b7cf;
    --ink-faint: #a5cde0;
    --map-tone: #2a719a;
  }
  * { box-sizing: border-box; margin: 0; padding: 0; }
  html, body { width: 848px; height: 1200px; overflow: hidden; background: var(--paper); }
  .sheet { position: relative; width: 848px; height: 1200px; font-family: "Roboto Slab", Georgia, serif; color: var(--ink-deep); }
  .title { position: absolute; top: 32px; left: 0; width: 100%; text-align: center; font-weight: 900; font-size: 74px; letter-spacing: 0.5px; color: var(--ink-deep); line-height: 1; }
  .section-heading { position: absolute; font-weight: 900; font-size: 18.5px; letter-spacing: 0.3px; color: var(--ink-deep); }
  .body-copy { position: absolute; font-size: 13.6px; line-height: 20.5px; text-align: justify; color: var(--ink-deep); }
  .geo-map { position: absolute; left: 40px; top: 356px; width: 765px; height: 310px; }
  .region-label { font-family: "Roboto Slab", Georgia, serif; font-weight: 700; font-size: 13px; fill: #fff; text-anchor: middle; }
  .region-value { font-family: "Roboto Slab", Georgia, serif; font-size: 12px; fill: #fff; text-anchor: middle; }
  .timer-set { position: absolute; left: 38px; top: 732px; width: 350px; height: 130px; }
  .timer-pct { font-family: "Roboto Slab", Georgia, serif; font-weight: 700; font-size: 10.5px; fill: #fff; text-anchor: middle; }
  .timer-name { font-family: "Roboto Slab", Georgia, serif; font-weight: 900; font-size: 11px; fill: var(--ink-deep); text-anchor: middle; }
  .viewer-figure { position: absolute; border-radius: 22px 22px 6px 6px; }
  .viewer-figure.male { left: 447px; top: 738px; width: 46px; height: 115px; background: var(--ink-deep); }
  .viewer-figure.female { left: 585px; top: 738px; width: 50px; height: 115px; background: var(--ink-soft); }
  .viewer-share { position: absolute; top: 818px; font-family: "Roboto", Arial, sans-serif; font-weight: 500; font-size: 33px; }
  .viewer-share.male { left: 497px; color: var(--ink-deep); }
  .viewer-share.female { left: 640px; color: var(--ink-soft); }
  .bar-list { position: absolute; left: 447px; top: 1020px; list-style: none; }
  .bar-row { display: flex; align-items: center; height: 25px; margin-bottom: 3.5px; }
  .bar { height: 25px; padding-left: 6px; font-family: "Roboto", Arial, sans-serif; font-weight: 500; font-size: 17px; line-height: 25px; color: #fff; }
  .bar-caption { margin-left: 6px; font-size: 13.6px; color: var(--ink-deep); }
  .composition { position: absolute; left: 38px; top: 950px; width: 345px; height: 215px; }
  .comp-name { font-family: "Roboto Slab", Georgia, serif; font-weight: 900; font-size: 10.5px; fill: var(--ink-deep); text-anchor: end; }
</style>
</head>
<body>
<main class="sheet">
  <h1 class="title">Title Goes Here</h1>

  <h2 class="section-heading" style="left:40px;top:166px;">OVERVIEW OF WHAT WE DID</h2>
  <p class="body-copy" style="left:40px;top:195px;width:375px;">Ferferio rporerro molore, cullum unt optas doloreni aut magnat facieni ut volo blabo. Illaut ant, vitiae ma volent quiaect otaquas pitaspe rciisti in con con cus. Optiberferepe volorro rerferor sus, serum quo</p>
  <p class="body-copy" style="left:435px;top:195px;width:373px;">quae cusdam fugiam, solutatust, volupti osaeperum quid ulluptatus il exerendant vellestiis moloribust volum que nectem. Coraecat. Um quisciis esequo exerit, corepre ratatqui diae.</p>

  <h2 class="section-heading" style="left:40px;top:318px;">GEOGRAPHICAL</h2>
  <svg class="geo-map" viewBox="0 0 765 310">
    <rect role="img" aria-label="World map showing viewer regions" x="0" y="0" width="765" height="310" rx="14" fill="var(--map-tone)"/>
    <circle cx="200" cy="147" r="66" fill="var(--ink-pale)" opacity="0.85"/>
    <circle cx="438" cy="94" r="75" fill="var(--ink-pale)" opacity="0.6"/>
    <circle cx="630" cy="169" r="52" fill="var(--ink-pale)" opacity="0.85"/>
    <text class="region-label" x="200" y="148">AMERICA</text>
    <text class="region-value" x="200" y="167">000,000</text>
    <text class="region-label" x="438" y="95">EUROPE</text>
    <text class="region-value" x="438" y="114">000,000</text>
    <text class="region-label" x="630" y="162">ASIA</text>
    <text class="region-value" x="630" y="180">000,000</text>
  </svg>

  <h2 class="section-heading" style="left:40px;top:698px;">COMPLETION RATE</h2>
  <svg class="timer-set" viewBox="0 0 350 130">
    <g transform="translate(43,56)">
      <rect x="-6" y="-47" width="12" height="9" rx="3" fill="none" stroke="var(--ink-deep)" stroke-width="3"/>
      <circle r="39" fill="none" stroke="var(--ink-deep)" stroke-width="5"/>
      <path d="M0 0 L0 -31 A31 31 0 1 1 -18.2 25.1 Z" fill="var(--ink-deep)"/>
      <text class="timer-pct" x="15" y="4">60%</text>
      <text class="timer-name" x="0" y="67">ABC</text>
    </g>
    <g transform="translate(170,56)">
      <rect x="-6" y="-47" width="12" height="9" rx="3" fill="none" stroke="var(--ink)" stroke-width="3"/>
      <circle r="39" fill="none" stroke="var(--ink)" stroke-width="5"/>
      <path d="M0 0 L0 -31 A31 31 0 1 1 -31 0 Z" fill="var(--ink)"/>
      <text class="timer-pct" x="13" y="4">75%</text>
      <text class="timer-name" x="0" y="67">DEF</text>
    </g>
    <g transform="translate(298,56)">
      <rect x="-6" y="-47" width="12" height="9" rx="3" fill="none" stroke="var(--ink-pale)" stroke-width="3"/>
      <circle r="39" fill="none" stroke="var(--ink-pale)" stroke-width="5"/>
      <path d="M0 0 L0 -31 A31 31 0 0 1 0 31 Z" fill="var(--ink-pale)"/>
      <text class="timer-pct" x="16" y="4" style="fill:var(--ink-deep)">50%</text>
      <text class="timer-name" x="0" y="67">HIJ</text>
    </g>
  </svg>

  <h2 class="section-heading" style="left:447px;top:698px;">NO. OF VIEWERS</h2>
  <div class="viewer-figure male" role="img" aria-label="Male viewer figure"></div>
  <div class="viewer-share male">48%</div>
  <div class="viewer-figure female" role="img" aria-label="Female viewer figure"></div>
  <div class="viewer-share female">52%</div>

  <p class="body-copy" style="left:447px;top:882px;width:361px;">Go me crum cre ima, es bontimis, Caturi turo, sena, non diemquem dici facci tesciorest Fora, se tes hocuro confeciemum vivirmis mo ute culocrit, patiocu llemquo. Bus, vid poere autereh empera aut cesse manum siliqui ssimure stalis; nosulut audepecto.</p>

  <ul class="bar-list">
    <li class="bar-row"><span class="bar" style="width:169px;background:var(--ink-deep);">XX%</span><span class="bar-caption">lorem ipsum si</span></li>
    <li class="bar-row"><span class="bar" style="width:84px;background:var(--ink);">XX%</span><span class="bar-caption">lorem ipsum si</span></li>
    <li class="bar-row"><span class="bar" style="width:56px;background:var(--ink-mid);">XX%</span><span class="bar-caption">lorem ipsum si</span></li>
    <li class="bar-row"><span class="bar" style="width:130px;background:var(--ink-soft);">XX%</span></li>
    <li class="bar-row"><span class="bar" style="width:158px;background:var(--ink-faint);">XX%</span><span class="bar-caption">lorem ipsum si</span></li>
  </ul>

  <h2 class="section-heading" style="left:40px;top:902px;">VIEWERS’ COMPOSITION</h2>
  <svg class="composition" viewBox="0 0 345 215">
    <g stroke="var(--ink-soft)" stroke-width="1" stroke-dasharray="2 2">
      <line x1="104" y1="4" x2="339" y2="4"/>
      <line x1="115" y1="54" x2="339" y2="54"/>
      <line x1="115" y1="105" x2="339" y2="105"/>
      <line x1="110" y1="145" x2="339" y2="145"/>
    </g>
    <circle cx="104" cy="108" r="102" fill="var(--ink-deep)"/>
    <circle cx="112" cy="129" r="81" fill="var(--ink)"/>
    <circle cx="105" cy="158" r="52" fill="var(--ink-soft)"/>
    <circle cx="104" cy="178" r="32" fill="#fff"/>
    <text class="comp-name" x="339" y="22">ABC</text>
    <text class="comp-name" x="339" y="36">50.3%</text>
    <text class="comp-name" x="339" y="63">DEF</text>
    <text class="comp-name" x="339" y="77">36.4%</text>
    <text class="comp-name" x="339" y="121">GHI</text>
    <text class="comp-name" x="339" y="135">12.9%</text>
    <text class="comp-name" x="339" y="161">JKL</text>
    <text class="comp-name" x="339" y="175">0.4%</text>
  </svg>
</main>
</body>
</html>
```